Brightwell Giving Inc

We need a full re-design of our non-profit organization website (www.brightwellgiving.org). Ideally, we are looking to make it more attractive, user-friendly, and interactive with our business model.

Please make sure to user colors that ago with our logo.

We need a homepage done and we also need a content page done where we will use for the other pages to fill with content.

Target Market(s)

Clothes/textiles donations.

Industry/Entity Type

Charity

Number of Pages Required

2 page

Colors

Designer to choose colors to be used in the design.

Requirements
Must have
• It must match the styling of our logo and same colors as current website. (www.brightwellgiving.org)
Nice to have
• Sleek homepage that is easy to understand and get our main points across.

```html
<!DOCTYPE html>
<html lang="en">
<head>
<meta charset="utf-8">
<title>Brightwell Giving — Home</title>
<link href="https://fonts.googleapis.com/css2?family=Roboto+Slab:wght@400;700&family=Roboto:ital,wght@0,400;0,500;0,700;1,400;1,500&display=swap" rel="stylesheet">
<style>
  :root {
    --green: #1e7d1e;
    --green-dark: #136113;
    --green-light: #5aa831;
    --ink: #2b2b2b;
    --muted: #7a7a7a;
    --line: #e4e4e4;
    --white: #ffffff;
    --page: #ffffff;
  }
  * { box-sizing: border-box; margin: 0; padding: 0; }
  html, body { width: 1200px; height: 900px; overflow: hidden; background: var(--page); }
  body { font-family: "Roboto", Arial, sans-serif; color: var(--ink); }

  .site { position: relative; width: 1200px; height: 900px; overflow: hidden; }

  /* Header */
  .site-header { height: 92px; display: flex; align-items: center; padding: 0 48px 0 62px; position: relative; }
  .brand { display: flex; align-items: center; gap: 10px; }
  .brand-mark { width: 26px; height: 26px; background: var(--green); }
  .brand-name { font-family: "Roboto Slab", Georgia, serif; font-weight: 700; font-size: 21px; color: var(--green); line-height: 1; text-transform: uppercase; }
  .brand-tagline { font-size: 10px; color: var(--muted); margin-top: 4px; font-style: italic; }

  .contact-list { display: flex; gap: 34px; margin-left: 90px; }
  .contact-item { display: flex; align-items: center; gap: 10px; }
  .contact-icon { width: 28px; height: 28px; border: 1px solid var(--line); border-radius: 50%; display: flex; align-items: center; justify-content: center; }
  .contact-label { font-family: "Roboto Slab", Georgia, serif; font-weight: 700; font-size: 12px; color: var(--green); font-style: italic; }
  .contact-value { font-size: 11px; color: var(--muted); margin-top: 2px; }

  .header-actions { margin-left: auto; display: flex; flex-direction: column; align-items: flex-end; gap: 10px; }
  .social { display: flex; align-items: center; gap: 8px; font-size: 12px; font-weight: 500; font-style: italic; color: var(--ink); }
  .social-dot { width: 20px; height: 20px; border-radius: 50%; background: #4a4a4a; }
  .donate-btn { background: var(--white); border: 2px solid var(--green); color: var(--green); font-weight: 700; font-style: italic; font-size: 13px; padding: 7px 22px; border-radius: 18px 0 18px 0; }

  /* Navigation */
  .main-nav { position: absolute; top: 80px; left: 62px; right: 200px; height: 38px; background: var(--green); border-radius: 0 0 14px 14px; display: flex; align-items: center; padding: 0 10px; z-index: 3; }
  .main-nav a { color: var(--white); text-decoration: none; font-size: 12.5px; font-weight: 500; font-style: italic; padding: 0 15px; height: 38px; display: flex; align-items: center; }
  .main-nav a.is-active { background: var(--green-light); border-radius: 0 0 10px 10px; }

  /* Hero */
  .hero { position: absolute; top: 92px; left: 0; width: 1200px; height: 660px; overflow: hidden; }
  .hero-photo { position: absolute; inset: 0;
    background:
      linear-gradient(90deg, rgba(0,0,0,0.55) 0%, rgba(0,0,0,0.25) 40%, rgba(0,0,0,0) 65%),
      radial-gradient(ellipse 320px 300px at 60% 52%, #5d8f3c 0%, rgba(93,143,60,0) 100%),
      linear-gradient(180deg, #6f8a5a 0%, #4f6a3e 45%, #7a6a55 78%, #5b4d3e 100%); }
  .hero-content { position: absolute; left: 62px; top: 200px; width: 330px; color: var(--white); }
  .hero-title { font-family: "Roboto Slab", Georgia, serif; font-weight: 700; font-size: 27px; line-height: 1.25; font-style: italic; }
  .hero-text { font-size: 12.5px; line-height: 1.6; margin-top: 16px; font-style: italic; opacity: .95; }
  .hero-btn { display: inline-block; margin-top: 22px; border: 1px solid var(--white); border-radius: 16px; padding: 6px 16px; font-size: 11.5px; font-weight: 500; color: var(--white); }
  .hero-arrow { position: absolute; top: 330px; width: 30px; height: 30px; border: 1px solid rgba(255,255,255,.8); border-radius: 50%; display: flex; align-items: center; justify-content: center; }
  .hero-arrow.prev { left: 20px; }
  .hero-arrow.next { right: 20px; }

  /* Volunteer bar */
  .volunteer-bar { position: absolute; top: 700px; left: 180px; width: 840px; height: 80px; background: var(--white); border-bottom: 3px solid var(--green-light); box-shadow: 0 6px 18px rgba(0,0,0,.12); display: flex; align-items: center; padding: 0 40px; z-index: 2; }
  .volunteer-title { font-family: "Roboto Slab", Georgia, serif; font-size: 19px; color: var(--ink); }
  .volunteer-title strong { color: var(--green); font-style: italic; }
  .volunteer-actions { margin-left: auto; display: flex; gap: 12px; }
  .btn-outline, .btn-solid { font-size: 12px; font-weight: 700; padding: 9px 22px; border-radius: 18px; }
  .btn-outline { border: 1.5px solid var(--green); color: var(--green); }
  .btn-solid { background: var(--green); color: var(--white); border: 1.5px solid var(--green); }

  /* About heading */
  .section-heading { position: absolute; top: 838px; left: 0; width: 1200px; display: flex; align-items: center; justify-content: center; gap: 14px; font-family: "Roboto Slab", Georgia, serif; font-size: 22px; color: var(--ink); }
  .section-heading strong { color: var(--green); }
  .section-heading::before, .section-heading::after { content: ""; width: 70px; height: 1px; background: var(--ink); }
</style>
</head>
<body>
<div class="site">
  <header class="site-header">
    <div class="brand">
      <span class="brand-mark"></span>
      <div>
        <div class="brand-name">Brightwell Giving</div>
        <div class="brand-tagline">Give clothes, share warmth</div>
      </div>
    </div>
    <div class="contact-list">
      <div class="contact-item">
        <span class="contact-icon">
          <svg width="12" height="12" viewBox="0 0 24 24"><path d="M6.6 10.8a15.2 15.2 0 0 0 6.6 6.6l2.2-2.2a1 1 0 0 1 1-.25 11.4 11.4 0 0 0 3.6.57 1 1 0 0 1 1 1V20a1 1 0 0 1-1 1A17 17 0 0 1 3 4a1 1 0 0 1 1-1h3.5a1 1 0 0 1 1 1c0 1.25.2 2.45.57 3.6a1 1 0 0 1-.25 1z" fill="#7a7a7a"/></svg>
        </span>
        <div>
          <div class="contact-label">Call Us:</div>
          <div class="contact-value">Toll Free: (800) 555-0142</div>
        </div>
      </div>
      <div class="contact-item">
        <span class="contact-icon">
          <svg width="12" height="12" viewBox="0 0 24 24"><rect x="2" y="5" width="20" height="14" rx="2" fill="none" stroke="#7a7a7a" stroke-width="2"/><path d="M2 6l10 7 10-7" fill="none" stroke="#7a7a7a" stroke-width="2"/></svg>
        </span>
        <div>
          <div class="contact-label">Email Us:</div>
          <div class="contact-value">info@brightwellgiving.org</div>
        </div>
      </div>
    </div>
    <div class="header-actions">
      <div class="social">Get Social <span class="social-dot"></span></div>
      <div class="donate-btn">Donate Now!</div>
    </div>
  </header>

  <nav class="main-nav">
    <a class="is-active">Home</a>
    <a>About Us</a>
    <a>Missions</a>
    <a>How It Works</a>
    <a>Family</a>
    <a>Sponsors</a>
    <a>News</a>
    <a>Wall of Needs</a>
    <a>Contact</a>
  </nav>

  <section class="hero">
    <div class="hero-photo" role="img" aria-label="Photo of a smiling child in a green shirt drawing at an outdoor table"></div>
    <div class="hero-content">
      <h1 class="hero-title">Brightwell Giving<br>Donated to Orphan House<br>in Ukraine</h1>
      <p class="hero-text">Brightwell Giving is a non-profit organization that was created for one purpose: helping the less fortunate in our country's time of greatest need...</p>
      <span class="hero-btn">Explore More</span>
    </div>
    <span class="hero-arrow prev"><svg width="10" height="10" viewBox="0 0 10 10"><path d="M7 1L3 5l4 4" fill="none" stroke="#fff" stroke-width="1.5"/></svg></span>
    <span class="hero-arrow next"><svg width="10" height="10" viewBox="0 0 10 10"><path d="M3 1l4 4-4 4" fill="none" stroke="#fff" stroke-width="1.5"/></svg></span>
  </section>

  <div class="volunteer-bar">
    <h2 class="volunteer-title">Are you ready to <strong>Volunteer?</strong></h2>
    <div class="volunteer-actions">
      <span class="btn-outline">Become a Volunteer</span>
      <span class="btn-solid">Make a Donation</span>
    </div>
  </div>

  <h2 class="section-heading">About <strong>Us</strong></h2>
</div>
</body>
</html>
```